Restricted Contest for Business Cards and Stationery
Restricted Contest for Business Cards and Stationery - Aviation
Use same font as used in my logo
Norman T. Whitby
President
40735 Cedar Hollow Lane Tampa, Florida 33418 U.S.A.
ntwhitby@corvanetrainers.com
www.corvanetrainers.com
Please create layouts for business cards, stationary and CD labels. Keep it clean and simple. I have uploaded two files. The file including the Peregrine Falcon Head, Wing and Lettering is our logo. Please consider using the second file, just the Peregrine Head, as a "water mark" for the letterhead. Please use a simple white background. Thank you.

```html
<!DOCTYPE html>
<html lang="en">
<head>
<meta charset="utf-8">
<title>Corvane Trainers Stationery</title>
<link href="https://fonts.googleapis.com/css2?family=Open+Sans:ital,wght@0,400;0,700;1,400;1,700&display=swap" rel="stylesheet">
<style>
  :root {
    --navy: #1b2850;
    --gold: #e3a51c;
    --ink: #333a48;
    --mark: #e8e8ea;
    --paper: #ffffff;
    --edge: #cfd2d8;
    --bg: #ffffff;
  }
  * { margin: 0; padding: 0; box-sizing: border-box; }
  html, body { width: 1200px; height: 849px; overflow: hidden; background: var(--bg); }
  body { position: relative; font-family: "Open Sans", Arial, sans-serif; color: var(--ink); }
  .piece { position: absolute; background: var(--paper); border: 1px solid var(--edge); overflow: hidden; }

  .brand-bar { position: absolute; display: flex; align-items: center; }
  .brand-name { font-weight: 700; color: var(--navy); letter-spacing: .04em; white-space: nowrap; line-height: 1; }
  .brand-dot { background: var(--gold); border-radius: 50%; flex: none; }
  .stripes { flex: 1; display: flex; flex-direction: column; }
  .stripe-navy { background: var(--navy); }
  .stripe-gold { background: var(--gold); }

  .watermark { position: absolute; background: radial-gradient(ellipse at 40% 45%, var(--mark) 0%, #f2f2f3 55%, rgba(255,255,255,0) 72%); }

  /* CD label */
  .cd-label { left: 14px; top: 116px; width: 298px; height: 298px; border-radius: 50%; }
  .cd-hole { position: absolute; left: 124px; top: 124px; width: 50px; height: 50px; border-radius: 50%; border: 1px solid var(--edge); background: var(--bg); }
  .cd-label .watermark { left: 130px; top: 10px; width: 170px; height: 150px; }
  .cd-label .brand-bar { left: 22px; top: 142px; right: 0; gap: 6px; }
  .cd-label .brand-name { font-size: 15px; }
  .cd-label .brand-dot { width: 9px; height: 9px; }
  .cd-label .stripe-navy { height: 7px; margin-bottom: 3px; }
  .cd-label .stripe-gold { height: 4px; }

  /* Business card */
  .business-card { left: 60px; top: 473px; width: 210px; height: 148px; }
  .business-card .brand-bar { left: 8px; top: 16px; right: 0; gap: 4px; }
  .business-card .brand-name { font-size: 11px; }
  .business-card .brand-dot { width: 7px; height: 7px; }
  .business-card .stripe-navy { height: 5px; margin-bottom: 2px; }
  .business-card .stripe-gold { height: 3px; }
  .card-details { position: absolute; left: 95px; top: 44px; font-size: 6.5px; line-height: 1.45; font-style: italic; }
  .card-name { font-size: 9px; font-weight: 700; color: var(--navy); }
  .card-title { font-size: 7px; color: var(--gold); margin-bottom: 7px; }
  .card-gap { height: 6px; }
  .card-web { font-weight: 700; color: var(--navy); font-style: normal; }

  /* Letterhead */
  .letterhead { left: 365px; top: 144px; width: 396px; height: 564px; }
  .letterhead .brand-bar { left: 28px; top: 28px; right: 12px; gap: 5px; }
  .letterhead .brand-name { font-size: 14px; }
  .letterhead .brand-dot { width: 8px; height: 8px; }
  .letterhead .stripe-navy { height: 6px; margin-bottom: 2px; }
  .letterhead .stripe-gold { height: 3px; }
  .letterhead .watermark { left: 0; top: 280px; width: 190px; height: 170px; }
  .footer-contact { position: absolute; right: 34px; bottom: 22px; font-size: 5px; line-height: 1.5; color: #666; }
  .footer-web { font-weight: 700; color: var(--navy); }

  /* Envelope front */
  .envelope-front { left: 773px; top: 276px; width: 415px; height: 204px; }
  .envelope-front .brand-bar { left: 18px; top: 24px; right: 0; gap: 5px; }
  .envelope-front .brand-name { font-size: 13px; }
  .envelope-front .brand-dot { width: 8px; height: 8px; }
  .envelope-front .stripe-navy { height: 6px; margin-bottom: 2px; }
  .envelope-front .stripe-gold { height: 3px; }
  .envelope-front .watermark { left: 90px; top: 50px; width: 170px; height: 150px; }

  /* Envelope back */
  .envelope-back { left: 773px; top: 499px; width: 415px; height: 209px; }
  .flap { position: absolute; left: 0; top: 0; width: 415px; height: 110px; }
  .envelope-back .footer-contact { right: 40px; bottom: 18px; }
</style>
</head>
<body>

<section class="piece cd-label" aria-label="CD label">
  <div class="watermark" role="img" aria-label="Faint bird head watermark"></div>
  <div class="brand-bar">
    <span class="brand-dot"></span>
    <span class="brand-name">CORVANE</span>
    <span class="stripes"><span class="stripe-navy"></span><span class="stripe-gold"></span></span>
  </div>
  <div class="cd-hole"></div>
</section>

<section class="piece business-card" aria-label="Business card">
  <div class="brand-bar">
    <span class="brand-dot"></span>
    <span class="brand-name">CORVANE</span>
    <span class="stripes"><span class="stripe-navy"></span><span class="stripe-gold"></span></span>
  </div>
  <div class="card-details">
    <p class="card-name">Norman T. Whitby</p>
    <p class="card-title">President</p>
    <p>40735 Cedar Hollow Lane</p>
    <p>Tampa, Florida 33418 U.S.A.</p>
    <div class="card-gap"></div>
    <p>Phone: +1 (813) 555-0148</p>
    <p>Email: ntwhitby@corvanetrainers.com</p>
    <div class="card-gap"></div>
    <p class="card-web">www.corvanetrainers.com</p>
  </div>
</section>

<section class="piece letterhead" aria-label="Letterhead">
  <div class="brand-bar">
    <span class="brand-dot"></span>
    <span class="brand-name">CORVANE</span>
    <span class="stripes"><span class="stripe-navy"></span><span class="stripe-gold"></span></span>
  </div>
  <div class="watermark" role="img" aria-label="Faint bird head watermark"></div>
  <div class="footer-contact">
    <p>40735 Cedar Hollow Lane</p>
    <p>Tampa, Florida 33418 U.S.A.</p>
    <p>Phone: +1 (813) 555-0148</p>
    <p class="footer-web">www.corvanetrainers.com</p>
  </div>
</section>

<section class="piece envelope-front" aria-label="Envelope front">
  <div class="brand-bar">
    <span class="brand-dot"></span>
    <span class="brand-name">CORVANE</span>
    <span class="stripes"><span class="stripe-navy"></span><span class="stripe-gold"></span></span>
  </div>
  <div class="watermark" role="img" aria-label="Faint bird head watermark"></div>
</section>

<section class="piece envelope-back" aria-label="Envelope back">
  <svg class="flap" viewBox="0 0 415 110" aria-hidden="true">
    <polyline points="0,0 207,108 415,0" fill="none" stroke="#cfd2d8" stroke-width="1"/>
  </svg>
  <div class="footer-contact">
    <p>40735 Cedar Hollow Lane</p>
    <p>Tampa, Florida 33418 U.S.A.</p>
    <p>Phone: +1 (813) 555-0149</p>
    <p class="footer-web">www.corvanetrainers.com</p>
  </div>
</section>

</body>
</html>
```